Rebrand existing website with new identity and colours as supplied

I have an old website that I would like updating with a new identity.
The website is at www.brackenvalefinancial.com
The new branding and changes are as set out below.

Target Market(s)

Buyers and sellers of SME businesses

Industry/Entity Type

Financial services

Coding

Coded - Design and coding required

Number of Pages Required

4 page

Requirements
Must have
• In addition to the small number of new pages I would like to retain the existing structure and pages - simply rebranded

```html
<!DOCTYPE html>
<html lang="en">
<head>
<meta charset="utf-8">
<title>Keystone Deal Advisory</title>
<link rel="stylesheet" href="https://fonts.googleapis.com/css2?family=Montserrat:wght@500;600;700;800&family=Lato:wght@400;700&family=Roboto:wght@400;500;700&display=swap">
<style>
:root{--navy:#131640;--navy-2:#1d2150;--red:#e2121f;--red-dark:#b50d16;--ink:#222;--muted:#555;--line:#d8d8d8;--white:#fff}
*{box-sizing:border-box;margin:0;padding:0}
html,body{width:1200px;height:4425px;overflow:hidden}
body{position:relative;background:var(--white);font-family:'Lato',sans-serif;color:var(--ink)}
.abs{position:absolute}
.btn{position:absolute;display:flex;align-items:center;justify-content:center;background:var(--red);color:var(--white);font:700 14px 'Montserrat',sans-serif;border-radius:4px;letter-spacing:.3px}
.btn.inline{position:relative;display:inline-flex}
.photo{position:absolute}
.h-sec{font:700 34px 'Montserrat',sans-serif;color:var(--navy)}
.tri{position:absolute;width:0;height:0;border-top:32px solid var(--red);border-left:32px solid transparent}
/* hero */
.hero-bg{position:absolute;left:0;top:0}
.logo{position:absolute;display:flex;align-items:center;gap:10px}
.logo .mark{width:14px;height:14px;background:var(--red)}
.logo .name{font:600 26px 'Montserrat',sans-serif;color:var(--white);line-height:1}
.logo .tag{font:400 9px 'Lato',sans-serif;color:#cfd0e0;margin-top:4px}
.nav{position:absolute;top:34px;left:428px;display:flex;gap:29px;font:700 14px 'Montserrat',sans-serif;color:var(--white)}
.nav .on{border-bottom:2px solid var(--white);padding-bottom:5px}
.hero-title{position:absolute;left:112px;top:190px;font:700 43px/52px 'Montserrat',sans-serif;color:var(--white)}
.dots{position:absolute;left:112px;top:533px;display:flex;gap:5px;align-items:center}
.dots i{display:block;width:11px;height:11px;border:1.5px solid var(--white);border-radius:50%}
.dots i.on{width:17px;height:17px;background:var(--white)}
/* welcome */
.welcome-text{position:absolute;left:620px;top:885px;width:470px}
.eyebrow{font:700 16px 'Montserrat',sans-serif;color:var(--red)}
.welcome-text h2{font:700 31px 'Montserrat',sans-serif;color:var(--navy);margin-top:10px;white-space:nowrap}
.welcome-text p{font:400 13.4px/21.5px 'Lato',sans-serif;color:var(--muted);text-align:justify;margin-top:14px}
.welcome-text .btn{width:146px;height:45px;margin-top:18px}
/* services */
.svc-title{position:absolute;top:1460px;width:1200px;text-align:center;font:700 34px 'Montserrat',sans-serif;color:var(--white)}
.card{position:absolute;width:235px;height:314px;display:flex;align-items:flex-end;justify-content:center;padding-bottom:30px;text-align:center;font:700 16px/20px 'Montserrat',sans-serif;color:var(--white)}
/* how */
.how{position:absolute;left:595px;top:2345px;width:493px;height:495px;background:var(--white);box-shadow:0 10px 40px rgba(0,0,0,.12)}
.how-text{position:absolute;left:650px;top:2410px;width:350px}
.how-text h2{margin-top:40px}
.how-text p{font:400 13.5px/21.5px 'Lato',sans-serif;color:var(--muted);margin-top:18px;text-align:justify}
.how-text .btn{width:145px;height:45px;margin-top:26px}
.dotgrid{position:absolute;background-image:radial-gradient(var(--navy) 1.3px,transparent 1.6px);background-size:12px 12px}
/* news */
.news-head{position:absolute;top:2925px;width:1200px;text-align:center}
.news-head p{font:400 14px 'Lato',sans-serif;color:var(--muted);margin-top:12px}
.news{position:absolute;top:3030px;width:310px;height:367px;background:var(--white);box-shadow:0 6px 24px rgba(0,0,0,.1)}
.news .ph{height:212px}
.news .d{font:400 13px 'Roboto',sans-serif;color:var(--muted);margin:22px 0 0 22px}
.news h3{font:500 20px/25px 'Roboto',sans-serif;color:var(--navy);margin:10px 22px 0}
.news .more{display:flex;align-items:center;gap:8px;font:700 13px 'Roboto',sans-serif;color:var(--navy);margin:14px 0 0 22px}
.news .more i{width:24px;height:24px;border-radius:50%;background:var(--red);color:#fff;font-style:normal;font-size:12px;display:flex;align-items:center;justify-content:center}
/* contact */
.form{position:absolute;left:432px;top:3617px;width:618px;height:423px;background:var(--white);box-shadow:0 8px 40px rgba(0,0,0,.12);padding:45px 45px 0}
.form h2{font:600 30px 'Montserrat',sans-serif;color:var(--navy)}
.field{position:absolute;width:250px}
.field label{display:block;font:700 13.5px 'Roboto',sans-serif;color:var(--navy)}
.field span{display:block;font:400 11.5px 'Roboto',sans-serif;color:#777;margin-top:17px;padding-bottom:7px;border-bottom:1px solid var(--line)}
.send{position:absolute;left:520px;top:320px;width:54px;height:54px;border-radius:50%;background:var(--red);display:flex;align-items:center;justify-content:center}
/* footer */
.fcol{position:absolute;top:4098px}
.fcol h4{font:700 20px 'Roboto',sans-serif;color:var(--white)}
.fcol .rule{position:relative;width:140px;height:1px;background:#6d7094;margin:22px 0 18px}
.fcol .rule::before{content:"";position:absolute;left:0;top:-4px;width:8px;height:8px;background:var(--red);transform:rotate(45deg)}
.fcol ul{list-style:none;font:400 13px/21.5px 'Roboto',sans-serif;color:#e3e4ee}
.social{display:flex;align-items:center;gap:12px;margin-bottom:12px;font:400 13px 'Roboto',sans-serif;color:#e3e4ee}
.social i{width:34px;height:34px;border-radius:50%;background:var(--white);display:block}
.copy{position:absolute;top:4372px;width:1200px;text-align:center;font:400 13px 'Roboto',sans-serif;color:#e3e4ee}
</style>
</head>
<body>

<!-- HERO -->
<svg class="hero-bg" width="1200" height="760" viewBox="0 0 1200 760">
  <defs>
    <linearGradient id="heroPhoto" x1="0" y1="0" x2="1" y2="1">
      <stop offset="0" stop-color="#6f7587"/><stop offset=".5" stop-color="#b7b9bd"/><stop offset="1" stop-color="#3a3b45"/>
    </linearGradient>
    <linearGradient id="navyFade" x1="0" x2="1"><stop offset=".45" stop-color="#131640"/><stop offset=".75" stop-color="#131640" stop-opacity=".1"/></linearGradient>
  </defs>
  <polygon points="0,0 1200,0 1200,560 335,730 0,590" fill="url(#heroPhoto)"/>
  <polygon points="0,0 1200,0 1200,560 335,730 0,590" fill="url(#navyFade)"/>
  <polygon points="48,632 335,730 1200,560 1200,573 335,745" fill="var(--red)"/>
  <rect x="810" y="70" width="390" height="610" fill="none" stroke="#1a1a1f" stroke-width="6" opacity=".5"/>
</svg>
<div class="photo" role="img" aria-label="Three business people reviewing documents at a desk in a bright office" style="left:470px;top:60px;width:700px;height:600px"></div>

<div class="logo" style="left:113px;top:20px">
  <div><div class="name">Keystone Deal</div><div class="tag">Advisory Ltd · help to buy or sell a business</div></div>
  <span class="mark"></span>
</div>
<nav class="nav"><span class="on">HOME</span><span>ABOUT US</span><span>SERVICES</span><span>BLOG</span><span>CONTACT US</span></nav>
<div class="btn" style="left:944px;top:20px;width:146px;height:46px">LET'S TALK</div>
<h1 class="hero-title">ALL THE HELP YOU<br>NEED TO BUY A<br>BUSINESS</h1>
<div class="btn" style="left:112px;top:357px;width:146px;height:47px">GET STARTED</div>
<div class="dots"><i class="on"></i><i></i><i></i><i></i></div>

<!-- WELCOME -->
<div class="abs" style="left:108px;top:888px;width:438px;height:329px;border:6px solid var(--red);border-right:none;border-bottom:none"></div>
<div class="abs" style="left:108px;top:888px;width:6px;height:329px;background:var(--red)"></div>
<div class="photo" role="img" aria-label="Business people shaking hands in a glass-walled meeting room" style="left:136px;top:913px;width:441px;height:332px;background:linear-gradient(135deg,#9aa4ae,#d9dde0 55%,#5d6470)"></div>
<div class="tri" style="left:625px;top:842px"></div>
<div class="welcome-text">
  <div class="eyebrow">WELCOME TO</div>
  <h2>KEYSTONE DEAL ADVISORY</h2>
  <p>It isn't every day that you purchase a business, and we appreciate that it can be a difficult time for both buyer and seller, often requiring a range of skills not needed at any other time in a business lifetime. Even after a price is agreed, agreeing the best split between up-front and deferred consideration can be vital in the success of a purchase both at completion and in the years ahead. Although there are many potential funders the right acquisition debt package can still be hard to find and complex to negotiate. That is where Keystone Deal Advisory can help, we have the tools, the experience, and the contacts to help you evaluate, structure, and fund your acquisition.</p>
  <div class="btn inline">LEARN MORE</div>
</div>

<!-- WHAT WE DO -->
<svg class="abs" style="left:0;top:1310px" width="1200" height="480" viewBox="0 0 1200 480">
  <polygon points="215,122 862,5 1100,115 1100,120 862,16 215,126" fill="var(--red)"/>
  <polygon points="0,160 200,132 862,22 1200,160 1200,480 0,480" fill="var(--navy)"/>
</svg>
<h2 class="svc-title">WHAT WE DO</h2>

<div class="card" role="img" aria-label="Man in a suit working at a desk" style="left:112px;top:1527px;background:linear-gradient(180deg,#8b7a70,#3a3336)">BUSINESS LOANS</div>
<div class="card" style="left:359px;top:1527px;background:linear-gradient(180deg,#c4121e,#5a0a10);align-items:center;flex-direction:column;justify-content:center;padding:0">
  <svg width="70" height="70" viewBox="0 0 70 70" fill="none" stroke="#fff" stroke-width="2.5"><circle cx="35" cy="24" r="13"/><path d="M35 16v16M31 20h6a3 3 0 0 1 0 6h-4a3 3 0 0 0 0 6h6"/><path d="M8 50l12-8h14l10 4M8 62l14-6h16l20-12"/></svg>
  <div style="margin-top:12px">BUSINESS CASH<br>ADVANCES</div>
</div>
<div class="card" role="img" aria-label="Two colleagues smiling at a laptop" style="left:606px;top:1527px;background:linear-gradient(180deg,#a8aeb0,#3e3f45)">REVOLVING CREDIT<br>FACILITIES</div>
<div class="card" role="img" aria-label="Hand using a laptop with financial charts" style="left:854px;top:1527px;background:linear-gradient(180deg,#c9cdd2,#4a4d56)">TAX BILL AND VAT<br>FUNDING</div>
<div class="card" role="img" aria-label="Tablet showing stock market charts" style="left:112px;top:1853px;background:linear-gradient(180deg,#243452,#0f1524)">TRADE FINANCE</div>
<div class="card" role="img" aria-label="Invoices and a calculator on a wooden desk" style="left:359px;top:1853px;background:linear-gradient(180deg,#6e5a48,#2b241f)">INVOICE FINANCE</div>
<div class="card" role="img" aria-label="Model house and documents on a table" style="left:606px;top:1853px;background:linear-gradient(180deg,#9d8f80,#3b3530)">COMMERCIAL<br>PROPERTY FINANCE</div>
<div class="card" role="img" aria-label="Hands pointing at charts on a laptop" style="left:854px;top:1853px;background:linear-gradient(180deg,#6b6861,#2a2926)">ASSET FINANCE</div>

<!-- HOW WE WORK -->
<div class="photo" role="img" aria-label="Hands discussing financial charts on a tablet and printouts" style="left:0;top:2272px;width:595px;height:563px;background:linear-gradient(135deg,#cfd6dc,#8ea3b5 50%,#e8ecef)"></div>
<div class="how"></div>
<div class="abs" style="left:1038px;top:2363px;width:67px;height:477px;border:18px solid var(--red);border-left:none"></div>
<div class="dotgrid" style="left:1030px;top:2775px;width:95px;height:97px"></div>
<div class="tri" style="left:650px;top:2412px"></div>
<div class="how-text">
  <h2 class="h-sec">HOW WE WORK</h2>
  <p>The Keystone Deal Advisory team have many years' experience as entrepreneurs, private equity investors, and senior lenders. We've bought, sold, founded, and funded many businesses over the last 40 years.</p>
  <p>We have developed the tools to identify the optimal structure for your deal, and we have the contacts to help you get it funded and completed.</p>
  <div class="btn inline">LEARN MORE</div>
</div>

<!-- NEWS -->
<div class="news-head">
  <h2 class="h-sec">OUR LATEST NEWS</h2>
  <p>Lorem ipsum dolor sit amet, consectetur sed do eiusmod tempor incididunt adipiscing elit</p>
</div>
<article class="news" style="left:110px">
  <div class="ph" role="img" aria-label="Tablet on a desk with a management word cloud and coffee" style="background:linear-gradient(135deg,#c9c2b4,#5a5a5e)"></div>
  <div class="d">May 3, 2021</div><h3>Lorem ipsum dolor sit am consectetur ad</h3><div class="more">Read more <i>›</i></div>
</article>
<article class="news" style="left:445px">
  <div class="ph" role="img" aria-label="Desk with a monitor showing stock charts" style="background:linear-gradient(135deg,#e6eaee,#8b96a3)"></div>
  <div class="d">May 3, 2021</div><h3>Lorem ipsum dolor sit am consectetur ad</h3><div class="more">Read more <i>›</i></div>
</article>
<article class="news" style="left:779px">
  <div class="ph" role="img" aria-label="Business people signing papers at a dark table" style="background:linear-gradient(135deg,#4a4640,#1f1d1b)"></div>
  <div class="d">May 3, 2021</div><h3>Lorem ipsum dolor sit am consectetur ad</h3><div class="more">Read more <i>›</i></div>
</article>
<div class="btn" style="left:503px;top:3425px;width:195px;height:48px">VIEW MORE NEWS</div>

<!-- CONTACT + FOOTER -->
<div class="abs" style="left:0;top:3835px;width:1200px;height:590px;background:var(--navy)"></div>
<div class="photo" role="img" aria-label="Hands working with a calculator and financial charts" style="left:110px;top:3575px;width:393px;height:330px;background:linear-gradient(135deg,#dfe3e6,#9fb0bf 55%,#6e7884)"></div>
<div class="dotgrid" style="left:85px;top:3860px;width:130px;height:75px;background-image:radial-gradient(#6d7094 1.3px,transparent 1.6px)"></div>
<div class="abs" style="left:775px;top:3572px;width:317px;height:300px;border:4px solid var(--red)"></div>
<form class="form">
  <h2>GET IN TOUCH</h2>
  <div class="field" style="left:45px;top:112px"><label>YOUR NAME</label><span>Jane Doe</span></div>
  <div class="field" style="left:320px;top:112px"><label>COMPANY</label><span>jane@keystonedeal.co</span></div>
  <div class="field" style="left:45px;top:200px"><label>EMAIL ADDRESS</label><span>jane@keystonedeal.co</span></div>
  <div class="field" style="left:320px;top:200px"><label>PHONE</label><span>1 888 888 888</span></div>
  <div class="field" style="left:45px;top:293px;width:460px"><label>MESSAGE</label><span>Hi , do you have a moment to talk about Us</span></div>
  <div class="send"><svg width="22" height="22" viewBox="0 0 24 24" fill="#fff"><path d="M22 2L2 10l7 3 3 7z"/></svg></div>
</form>

<div class="logo" style="left:110px;top:4128px">
  <div><div class="name" style="font-size:30px">Keystone Deal</div><div class="tag">Advisory Ltd · help to buy or sell a business</div></div>
  <span class="mark"></span>
</div>
<div class="fcol" style="left:445px"><h4>Find Out More</h4><div class="rule"></div>
  <ul><li>About us</li><li>Our People and Our Team</li><li>Our Clients</li><li>Contact us</li><li>Careers</li></ul></div>
<div class="fcol" style="left:693px"><h4>Quick links</h4><div class="rule"></div>
  <ul><li>Home</li><li>About</li><li>Working Capital Finance</li><li>Asset Finance</li><li>Property Finance</li><li>Contact</li></ul></div>
<div class="fcol" style="left:947px"><h4>Follow us</h4><div class="rule"></div>
  <div class="social"><i></i>Chatterly</div>
  <div class="social"><i></i>Workweave</div></div>
<div class="copy">© 2022 Company name.All Rights Reserved &nbsp;| Privacy Policy | &nbsp;Terms</div>

</body>
</html>
```